Tamarack Hearth Partners Business Card

Looking for a new business card layout. We are a real estate firm w/ a logo, old design attached. Must keep the same elements on there, just need a fresh look and possible some foil accents. Looking for a simpler design w/ more modern style.

Target Market(s)

Real Estate clients

Industry/Entity Type

Real Estate Agent

Contact Information for Business Card

see attached

Font styles to use
Sans Serif

Requirements
Must have
• all elements on current biz card
Nice to have
• modern look, simpler than we have!
Should not have
• no serif fonts

```html
<!DOCTYPE html>
<html lang="en">
<head>
<meta charset="utf-8">
<title>Tamarack Hearth Partners Business Card</title>
<link href="https://fonts.googleapis.com/css2?family=Montserrat:wght@500;600;700&display=swap" rel="stylesheet">
<style>
  :root {
    --backdrop: #7790c8;
    --card-dark: #111111;
    --card-light: #ffffff;
    --brand-blue: #0aa0e6;
    --brand-cyan: #14c8e6;
    --text-light: #ffffff;
    --photo-top: #e9e4d6;
    --photo-mid: #d9b98a;
    --photo-bottom: #3cc4c8;
  }
  * { box-sizing: border-box; margin: 0; padding: 0; }
  html, body {
    width: 1200px; height: 1200px; overflow: hidden;
    background: var(--backdrop);
    font-family: "Montserrat", sans-serif;
  }
  .canvas { position: relative; width: 1200px; height: 1200px; }
  .card {
    position: absolute; width: 805px; height: 461px;
    border-radius: 37px; overflow: hidden;
    box-shadow: 0 6px 14px rgba(30, 40, 80, 0.25);
  }
  .card-front { left: 198px; top: 102px; background: var(--card-dark); }
  .card-back { left: 222px; top: 655px; background: var(--card-light); }

  .portrait {
    position: absolute; left: 0; top: 0; width: 356px; height: 100%;
    background: linear-gradient(180deg, var(--photo-top) 0%, var(--photo-mid) 50%, var(--photo-bottom) 100%);
  }

  .brand { position: absolute; display: flex; align-items: center; }
  .brand-dot { border-radius: 50%; background: var(--brand-blue); flex: none; }
  .brand-name {
    color: var(--brand-blue); font-weight: 700; text-transform: uppercase;
    line-height: 1.05; letter-spacing: 0.06em;
  }
  .card-front .brand { left: 454px; top: 36px; gap: 20px; }
  .card-front .brand-dot { width: 92px; height: 92px; }
  .card-front .brand-name { font-size: 21px; }
  .card-back .brand { left: 216px; top: 160px; gap: 36px; }
  .card-back .brand-dot { width: 150px; height: 150px; }
  .card-back .brand-name { font-size: 34px; }

  .details {
    position: absolute; right: 80px; top: 178px;
    text-align: right; color: var(--text-light);
  }
  .agent-name { font-size: 28px; font-weight: 700; letter-spacing: 0.08em; }
  .agent-title { font-size: 15px; font-weight: 600; letter-spacing: 0.2em; margin-top: 8px; }
  .address { font-size: 13px; font-weight: 600; letter-spacing: 0.1em; line-height: 14px; margin-top: 28px; }

  .contact-list { position: absolute; right: 48px; top: 306px; list-style: none; }
  .contact-item {
    display: flex; align-items: center; justify-content: flex-end;
    height: 20px; margin-bottom: 13px;
    color: var(--text-light); font-size: 13px; font-weight: 600; letter-spacing: 0.14em;
  }
  .contact-icon {
    width: 20px; height: 20px; margin-left: 12px; border-radius: 50%;
    background: var(--brand-cyan); display: flex; align-items: center; justify-content: center;
  }
  .contact-icon svg { width: 12px; height: 12px; }
</style>
</head>
<body>
<div class="canvas">
  <section class="card card-front">
    <div class="portrait" role="img" aria-label="Portrait photo of the agent"></div>

    <div class="brand">
      <span class="brand-dot"></span>
      <span class="brand-name">Tamarack<br>Hearth<br>Partners</span>
    </div>

    <div class="details">
      <h1 class="agent-name">Dana Whitfield</h1>
      <p class="agent-title">Principal Broker</p>
      <p class="address">482 NW Larch Ave<br>Sisters,OR 97759</p>
    </div>

    <ul class="contact-list">
      <li class="contact-item">555.204.7180
        <span class="contact-icon"><svg viewBox="0 0 12 12"><path d="M3 1.5 L4.6 3.6 L3.8 4.8 C4.4 6.2 5.6 7.4 7.2 8.2 L8.4 7.4 L10.5 9 L9.5 10.5 C5.5 10.2 1.8 6.5 1.5 2.5 Z" fill="#111"/></svg></span>
      </li>
      <li class="contact-item">555.318.6642
        <span class="contact-icon"><svg viewBox="0 0 12 12"><rect x="3.2" y="1" width="5.6" height="10" rx="1" fill="none" stroke="#111" stroke-width="1.2"/><circle cx="6" cy="9.3" r="0.6" fill="#111"/></svg></span>
      </li>
      <li class="contact-item">dana@tamarackhearth.com
        <span class="contact-icon"><svg viewBox="0 0 12 12"><rect x="1.2" y="2.8" width="9.6" height="6.6" fill="none" stroke="#111" stroke-width="1.1"/><path d="M1.4 3 L6 6.6 L10.6 3" fill="none" stroke="#111" stroke-width="1.1"/></svg></span>
      </li>
      <li class="contact-item">www.tamarackhearthpartners.com
        <span class="contact-icon"><svg viewBox="0 0 12 12"><circle cx="6" cy="6" r="4.6" fill="none" stroke="#111" stroke-width="1.1"/><ellipse cx="6" cy="6" rx="2" ry="4.6" fill="none" stroke="#111" stroke-width="0.9"/><path d="M1.4 6 H10.6" stroke="#111" stroke-width="0.9"/></svg></span>
      </li>
    </ul>
  </section>

  <section class="card card-back">
    <div class="brand">
      <span class="brand-dot"></span>
      <span class="brand-name">Tamarack<br>Hearth<br>Partners</span>
    </div>
  </section>
</div>
</body>
</html>
```